bottle label/ product label for smoothies (ultra fresh)

Please create a bottle label for our smoothies for retail distribution.
It's important that the following key features are clearly stated:

Ultra-fresh

Handmade

No preservatives

Not heat-treated

No added sugar

The base of the product label should be transparent, so that the color and content of the smoothie can be seen clearly.

We are a young, dynamic company. Our values are honesty, ultra-freshness, and authenticity — and we are the only ones producing this type of product in our country. We are positioned in the premium segment.

Design style: Modern, clean, and natural — but not playful or childish.

Example product: Kelu Kelu (Mango, Pineapple, Lemon, Passion Fruit, Orange)

Wenn du möchtest, kann ich auch gleich einen konkreten Vorschlag für das Etikettendesign auf Englisch oder einen Entwurfstext für das Label selbst erstellen. Sag einfach Bescheid!

Target Market(s)

trade - convenience

Industry/Entity Type

trade

Font styles to use
Sans Serif

Requirements
Must have
• sales- features: Ultra-fresh Handmade No preservatives Not heat-treated No added sugar

```html
<!DOCTYPE html>
<html lang="en">
<head>
<meta charset="utf-8">
<title>Velora – Ultra Fresh Mango Smoothie Label</title>
<link rel="stylesheet" href="https://fonts.googleapis.com/css2?family=Poppins:wght@600&family=Inter:wght@400;500;600;700&family=Lilita+One&display=swap">
<style>
  :root {
    --backdrop: #b9b8b0;
    --label: #c99a2e;
    --label-deep: #bb8a22;
    --ink-light: #ebe9e4;
    --ink-dark: #1d1a15;
    --line-art: rgba(235, 233, 228, 0.55);
  }
  * { box-sizing: border-box; margin: 0; padding: 0; }
  html, body { width: 1200px; height: 827px; overflow: hidden; }
  body {
    background: var(--backdrop);
    display: flex;
    align-items: center;
    justify-content: center;
    font-family: "Inter", sans-serif;
  }
  .label {
    width: 470px;
    height: 770px;
    background: var(--label);
    border-radius: 10px;
    padding: 40px 44px 32px;
    display: flex;
    flex-direction: column;
    align-items: center;
    color: var(--ink-light);
  }
  .brand {
    font-family: "Poppins", sans-serif;
    font-weight: 600;
    font-size: 62px;
    line-height: 1;
    letter-spacing: 0.5px;
    color: var(--ink-dark);
  }
  .brand-tagline {
    font-family: "Inter", sans-serif;
    font-weight: 600;
    font-size: 16px;
    letter-spacing: 5px;
    color: var(--ink-dark);
    margin-top: 6px;
  }
  .claim {
    font-weight: 500;
    font-size: 30px;
    letter-spacing: 1px;
    margin-top: 18px;
  }
  .product-name {
    font-family: "Lilita One", sans-serif;
    font-size: 104px;
    line-height: 0.9;
    letter-spacing: 2px;
    margin-top: 4px;
  }
  .product-type {
    font-family: "Lilita One", sans-serif;
    font-size: 50px;
    line-height: 1;
    letter-spacing: 2px;
  }
  .fruit-illustration {
    width: 100%;
    height: 190px;
    margin-top: 14px;
    border-radius: 6px;
    background: radial-gradient(circle at 50% 50%, var(--label-deep) 0 30%, var(--label) 70%);
    border: 1px solid var(--line-art);
  }
  .blend-note {
    font-weight: 500;
    font-size: 36px;
    letter-spacing: 0.5px;
    margin-top: 16px;
  }
  .features {
    display: flex;
    justify-content: space-between;
    width: 100%;
    margin-top: 14px;
    list-style: none;
  }
  .feature {
    width: 25%;
    display: flex;
    flex-direction: column;
    align-items: center;
    text-align: center;
    font-size: 11px;
    font-weight: 500;
    line-height: 1.2;
  }
  .feature svg { width: 46px; height: 46px; margin-bottom: 5px; }
  .slogan {
    font-weight: 700;
    font-size: 19px;
    letter-spacing: 4px;
    margin-top: 16px;
  }
  .volume {
    font-weight: 700;
    font-size: 22px;
    margin-top: 6px;
  }
</style>
</head>
<body>
  <main class="label">
    <div class="brand">Velora</div>
    <div class="brand-tagline">Hand Maded</div>
    <div class="claim">ULTRA FRESH</div>
    <h1 class="product-name">MANGO</h1>
    <div class="product-type">SMOOTHI</div>
    <div class="fruit-illustration" role="img" aria-label="Line illustration of mango, pineapple and citrus fruits around a central mango"></div>
    <div class="blend-note">PURE BLENDED</div>
    <ul class="features">
      <li class="feature">
        <svg viewBox="0 0 46 46" fill="none" stroke="currentColor" stroke-width="2" stroke-linecap="round">
          <circle cx="23" cy="23" r="21"/>
          <path d="M14 31c0-10 8-17 18-17 0 10-7 17-18 17z"/>
          <path d="M14 31l10-9"/>
        </svg>
        Ultra-fresh
      </li>
      <li class="feature">
        <svg viewBox="0 0 46 46" fill="none" stroke="currentColor" stroke-width="2" stroke-linecap="round">
          <circle cx="23" cy="23" r="21"/>
          <rect x="14" y="14" width="9" height="9"/>
          <rect x="23" y="23" width="9" height="9"/>
          <path d="M8 8l30 30"/>
        </svg>
        No Sugar
      </li>
      <li class="feature">
        <svg viewBox="0 0 46 46" fill="none" stroke="currentColor" stroke-width="2" stroke-linecap="round">
          <circle cx="23" cy="23" r="21"/>
          <path d="M19 11h8M20 11v7l-5 6v11h16V24l-5-6v-7"/>
          <path d="M8 8l30 30"/>
        </svg>
        No Preservatives
      </li>
      <li class="feature">
        <svg viewBox="0 0 46 46" fill="none" stroke="currentColor" stroke-width="2" stroke-linecap="round">
          <circle cx="23" cy="23" r="21"/>
          <path d="M20 27V12a3 3 0 0 1 6 0v15a6 6 0 1 1-6 0z"/>
          <path d="M8 8l30 30"/>
        </svg>
        Not Heat-Treated
      </li>
    </ul>
    <div class="slogan">Pioneering pure taste</div>
    <div class="volume">100ml</div>
  </main>
</body>
</html>
```